Solace Chiropractic & Acupuncture Business Cards

I need a business card design that feels elevated. I am open to any of the logo designs uploaded. We have two doctors so I'll need to be able to change out the names.

Information:
Marnie Toller D.C., Dipl. Ac. ASA
584 W 12th St, Ste 320
Alder Falls, ND 67419
solacegrove.net
620-555-0147
drmarnie@solacegrove.com
Updates

We have designs we like now, we are just trying to choose between top contenders. Thanks for your submissions!

Contact Information for Business Card

noted in description

Requirements
Must have
• ability to edit info if possible
Nice to have
• Please see our website solacegrove.net for our style and colors

```html
<!DOCTYPE html>
<html lang="en">
<head>
<meta charset="utf-8">
<title>Solace Chiropractic &amp; Acupuncture – Business Card</title>
<link rel="stylesheet" href="https://fonts.googleapis.com/css2?family=Source+Sans+3:wght@300;400&display=swap">
<style>
  :root {
    --backdrop: #d6d5d1;
    --card: #f4f3ee;
    --ink: #2d323e;
    --ink-soft: #3a3f4a;
    --rule: #b9b9b6;
  }
  html, body {
    margin: 0;
    padding: 0;
    width: 1200px;
    height: 692px;
    overflow: hidden;
    background: var(--backdrop);
  }
  .card {
    position: absolute;
    left: 40px;
    top: 26px;
    width: 1120px;
    height: 640px;
    background: var(--card);
    font-family: "Source Sans 3", "Helvetica Neue", Arial, sans-serif;
    color: var(--ink);
  }
  .brand {
    position: absolute;
    left: 72px;
    top: 218px;
    width: 460px;
    font-weight: 300;
    color: var(--ink);
  }
  .brand-name {
    display: block;
    font-size: 118px;
    line-height: 1;
    letter-spacing: 1px;
  }
  .brand-tagline {
    display: block;
    margin-top: 8px;
    padding-left: 120px;
    font-size: 16px;
    letter-spacing: 1.2px;
    text-transform: uppercase;
  }
  .divider {
    position: absolute;
    left: 570px;
    top: 125px;
    width: 1px;
    height: 382px;
    background: var(--rule);
  }
  .contact {
    position: absolute;
    left: 622px;
    top: 126px;
    color: var(--ink-soft);
    font-weight: 400;
  }
  .doctor-name {
    margin: 0;
    font-size: 34px;
    line-height: 46px;
    font-weight: 400;
    color: var(--ink);
  }
  .credentials {
    font-size: 26px;
    font-weight: 400;
  }
  .name-rule {
    width: 190px;
    height: 1px;
    margin: 16px 0 0;
    border: 0;
    background: var(--rule);
  }
  .address,
  .links {
    margin: 0;
    font-size: 31px;
    line-height: 43px;
    font-style: normal;
  }
  .address { margin-top: 36px; }
  .links { margin-top: 46px; }
  .links span { display: block; }
</style>
</head>
<body>
  <main class="card">
    <div class="brand">
      <span class="brand-name">Solace</span>
      <span class="brand-tagline">Chiropractic &amp; Acupuncture</span>
    </div>

    <div class="divider"></div>

    <section class="contact">
      <h1 class="doctor-name">Marnie Toller <span class="credentials">D.C., Dipl. Ac. ASA</span></h1>
      <hr class="name-rule">
      <address class="address">
        584 W 12th St, Ste 320<br>
        Alder Falls, ND 67419
      </address>
      <p class="links">
        <span>solacegrove.net</span>
        <span>620-555-0147</span>
        <span>drmarnie@solacegrove.com</span>
      </p>
    </section>
  </main>
</body>
</html>
```